Brightwell Dental Appointment Cards

This is a sister company of Larkspur Dental Group
We are a returning client.
This is what we like:
We like Pembrooke
Pembrooke font is cool
our Client is mostly Hispanic
We like to put Dr. Okafor, QXVU Graduate
Please look at Larkspur Dental Appt. Cards/Business Cards
Updates

We would like to see new logos, too.

Industry/Entity Type

Dental

Contact Information for Business Card

Tobi R. Okafor, D.D.S
QXVU Graduate
2374 West Quill Ave., Suite 210
Fernhollow, WQ 90417

Colors

Designer to choose colors to be used in the design.

Requirements
Nice to have
• Pembrooke Features

```html
<!DOCTYPE html>
<html lang="en">
<head>
<meta charset="utf-8">
<title>Brightwell Dental – Business Card</title>
<link rel="stylesheet" href="https://fonts.googleapis.com/css2?family=Bebas+Neue&family=Poppins:wght@600&display=swap">
<style>
  :root {
    --page: #ffffff;
    --blue-deep: #0a4c98;
    --blue-bright: #00a9e9;
    --blue-line: #0d4f9e;
    --blue-stripe: #1fa8e6;
    --grey-light: #e8e8e8;
    --grey-mid: #c4c4c4;
    --grey-edge: #a6a6a6;
    --name-blue: #6ec8f2;
    --text-white: #ffffff;
    --shadow: rgba(0, 0, 0, 0.55);
    --motif: rgba(255, 255, 255, 0.22);
  }
  html, body {
    margin: 0;
    padding: 0;
    width: 1200px;
    height: 804px;
    overflow: hidden;
    background: var(--page);
  }
  .card {
    display: block;
    width: 1200px;
    height: 804px;
  }
  .card__name {
    font-family: "Bebas Neue", "Arial Narrow", sans-serif;
    font-size: 73px;
    fill: var(--name-blue);
    letter-spacing: 0.5px;
  }
  .card__credential,
  .card__address {
    font-family: "Poppins", "Century Gothic", sans-serif;
    font-weight: 600;
    fill: var(--text-white);
  }
  .card__credential { font-size: 29px; }
  .card__address { font-size: 40px; letter-spacing: 0.5px; }
</style>
</head>
<body>
<svg class="card" viewBox="0 0 1242 832" preserveAspectRatio="none" xmlns="http://www.w3.org/2000/svg">
  <defs>
    <radialGradient id="grey-field" cx="0.52" cy="0.5" r="0.6">
      <stop offset="0" stop-color="var(--grey-light)"/>
      <stop offset="0.6" stop-color="var(--grey-mid)"/>
      <stop offset="1" stop-color="var(--grey-edge)"/>
    </radialGradient>
    <radialGradient id="blue-glow-top" cx="0.55" cy="0.3" r="0.7">
      <stop offset="0" stop-color="var(--blue-bright)"/>
      <stop offset="1" stop-color="var(--blue-deep)"/>
    </radialGradient>
    <radialGradient id="blue-glow-bottom" cx="0.5" cy="0.9" r="0.7">
      <stop offset="0" stop-color="var(--blue-bright)"/>
      <stop offset="1" stop-color="var(--blue-deep)"/>
    </radialGradient>
    <filter id="text-shadow" x="-5%" y="-20%" width="115%" height="160%">
      <feDropShadow dx="3" dy="4" stdDeviation="3" flood-color="var(--shadow)"/>
    </filter>
    <filter id="band-shadow" x="-5%" y="-20%" width="110%" height="140%">
      <feDropShadow dx="0" dy="4" stdDeviation="4" flood-color="rgba(0,0,0,0.35)"/>
    </filter>
  </defs>

  <rect class="card__field" x="35" y="33" width="1172" height="762" fill="url(#grey-field)"/>

  <rect class="card__motif" x="40" y="310" width="390" height="350" rx="170" fill="var(--motif)"
        role="img" aria-label="Faint decorative motif on the grey field"/>

  <g class="card__band card__band--top" filter="url(#band-shadow)">
    <polygon points="35,33 1207,33 1207,262 656,262 556,110 35,110" fill="url(#blue-glow-top)"/>
  </g>
  <path class="card__stripe" d="M35,127 L548,123" stroke="var(--blue-stripe)" stroke-width="13" fill="none"/>
  <path class="card__rule" d="M548,122 L648,272 L1207,276" stroke="var(--blue-line)" stroke-width="4" fill="none"/>
  <path class="card__rule" d="M560,140 L635,262" stroke="var(--blue-line)" stroke-width="2" fill="none"/>
  <path class="card__stripe" d="M652,282 L1207,285" stroke="var(--blue-stripe)" stroke-width="14" fill="none"/>

  <path class="card__stripe" d="M35,646 L578,652" stroke="var(--blue-stripe)" stroke-width="14" fill="none"/>
  <g class="card__band card__band--bottom">
    <polygon points="35,668 583,660 693,742 1207,742 1207,795 35,795" fill="url(#blue-glow-bottom)"/>
  </g>
  <path class="card__rule" d="M580,656 L690,731 L1207,734" stroke="var(--blue-line)" stroke-width="4" fill="none"/>
  <path class="card__rule" d="M605,656 L680,718" stroke="var(--blue-line)" stroke-width="2" fill="none"/>
  <path class="card__stripe" d="M690,736 L1207,738" stroke="var(--blue-stripe)" stroke-width="10" fill="none"/>

  <text class="card__name" x="55" y="258" filter="url(#text-shadow)">Tobi R. Okafor, D.D.S</text>
  <text class="card__credential" x="60" y="302" filter="url(#text-shadow)">QXVU Graduate</text>
  <text class="card__address" x="1140" y="576" text-anchor="end" filter="url(#text-shadow)">2374 West Quill Ave., Suite 210</text>
  <text class="card__address" x="1140" y="630" text-anchor="end" filter="url(#text-shadow)">Fernhollow, WQ 90417</text>
</svg>
</body>
</html>
```